business cards for Tramvex
Tramvexa
business cards for Tramvex - Government
Modern
R.K.Dunmore
914 E Harlan Avenue, Suite 215 Fort Worth, TX 76102
rdunmore@tramvexa-mail.com
www.tramvexa-site.com
need to be able to create cards for other people- the backside is logo only- the front needs my name then tramvexa with address email phone number and website- please put logo on front side as well. colors can be red/white/blue/ black or any combination
big version of logo and possibly ability to write on it- this may not work out well so if it doesn't then don't do it.

```html
<!DOCTYPE html>
<html lang="en">
<head>
<meta charset="utf-8">
<title>Tramvexa Business Cards</title>
<link rel="stylesheet" href="https://fonts.googleapis.com/css2?family=Montserrat:wght@400;500;600;700&display=swap">
<style>
  :root {
    --backdrop: #e9eaec;
    --card: #ffffff;
    --navy: #1f2f5c;
    --red: #a3283a;
    --accent-blue: #2d7fb4;
    --ink: #2b2b2b;
    --muted: #5a5f6a;
  }
  * { box-sizing: border-box; margin: 0; padding: 0; }
  html, body {
    width: 1200px; height: 895px; overflow: hidden;
    background: var(--backdrop);
    font-family: "Montserrat", sans-serif;
  }
  .sheet {
    width: 1200px; height: 895px;
    display: flex; flex-direction: column; align-items: center; justify-content: center;
    gap: 56px;
  }
  .card {
    position: relative;
    width: 640px; height: 366px;
    background: var(--card);
    box-shadow: 0 6px 18px rgba(0,0,0,0.12);
    overflow: hidden;
  }
  .brand { display: flex; align-items: center; gap: 12px; }
  .brand-mark { width: 30px; height: 30px; background: var(--navy); }
  .brand-name { font-weight: 700; color: var(--navy); letter-spacing: 1px; }

  /* front */
  .card-front .brand { position: absolute; left: 150px; top: 44px; }
  .card-front .brand-name { font-size: 40px; }
  .person { position: absolute; left: 150px; top: 116px; }
  .person-name { font-size: 21px; font-weight: 600; color: var(--accent-blue); letter-spacing: 2px; text-transform: uppercase; }
  .person-title { margin-top: 4px; font-size: 13px; font-weight: 600; color: var(--ink); letter-spacing: 2px; text-transform: uppercase; }
  .contact { position: absolute; top: 192px; list-style: none; font-size: 12.5px; color: var(--muted); }
  .contact li { display: flex; align-items: flex-start; gap: 10px; margin-bottom: 10px; line-height: 1.35; }
  .contact svg { flex: none; width: 14px; height: 14px; margin-top: 1px; fill: var(--muted); }
  .contact-left { left: 50px; width: 280px; }
  .contact-right { left: 380px; top: 232px; }
  .stripe { position: absolute; height: 7px; }
  .stripe-red { left: 50px; top: 292px; width: 300px; background: var(--red); }
  .stripe-navy { left: 350px; top: 330px; width: 290px; background: var(--navy); }

  /* back */
  .card-back { display: flex; align-items: center; justify-content: center; }
  .card-back .brand-mark { width: 44px; height: 44px; }
  .card-back .brand-name { font-size: 52px; }
</style>
</head>
<body>
<main class="sheet">
  <section class="card card-front" aria-label="Business card front">
    <div class="brand">
      <span class="brand-mark"></span>
      <span class="brand-name">Tramvexa</span>
    </div>
    <div class="person">
      <p class="person-name">Owen Callister</p>
      <p class="person-title">General Manager</p>
    </div>
    <ul class="contact contact-left">
      <li>
        <svg viewBox="0 0 24 24"><path d="M12 2a7 7 0 0 0-7 7c0 5 7 13 7 13s7-8 7-13a7 7 0 0 0-7-7zm0 9.5a2.5 2.5 0 1 1 0-5 2.5 2.5 0 0 1 0 5z"/></svg>
        <span>914 E Harlan Avenue, Suite 215<br>Fort Worth, TX 76102</span>
      </li>
      <li>
        <svg viewBox="0 0 24 24"><path d="M12 2a10 10 0 1 0 0 20 10 10 0 0 0 0-20zm6.9 6h-3a15 15 0 0 0-1.3-3.9A8 8 0 0 1 18.9 8zM12 4c.8 1.2 1.5 2.5 1.9 4h-3.8c.4-1.5 1.1-2.8 1.9-4zM4.3 14a8 8 0 0 1 0-4h3.4a16 16 0 0 0 0 4zm.8 2h3a15 15 0 0 0 1.3 3.9A8 8 0 0 1 5.1 16zm3-8h-3a8 8 0 0 1 4.3-3.9A15 15 0 0 0 8.1 8zM12 20c-.8-1.2-1.5-2.5-1.9-4h3.8c-.4 1.5-1.1 2.8-1.9 4zm2.3-6H9.7a14 14 0 0 1 0-4h4.6a14 14 0 0 1 0 4zm.3 5.9a15 15 0 0 0 1.3-3.9h3a8 8 0 0 1-4.3 3.9zm1.7-5.9a16 16 0 0 0 0-4h3.4a8 8 0 0 1 0 4z"/></svg>
        <span>www.tramvexa-site.com</span>
      </li>
    </ul>
    <ul class="contact contact-right">
      <li>
        <svg viewBox="0 0 24 24"><path d="M6.6 10.8a15 15 0 0 0 6.6 6.6l2.2-2.2a1 1 0 0 1 1-.25 11.4 11.4 0 0 0 3.6.6 1 1 0 0 1 1 1V20a1 1 0 0 1-1 1A17 17 0 0 1 3 4a1 1 0 0 1 1-1h3.5a1 1 0 0 1 1 1c0 1.25.2 2.45.6 3.6a1 1 0 0 1-.25 1z"/></svg>
        <span>012 555 0147</span>
      </li>
      <li>
        <svg viewBox="0 0 24 24"><path d="M16 1H8a2 2 0 0 0-2 2v18a2 2 0 0 0 2 2h8a2 2 0 0 0 2-2V3a2 2 0 0 0-2-2zm0 17H8V4h8zm-4 3.5a1 1 0 1 1 0-2 1 1 0 0 1 0 2z"/></svg>
        <span>012 555 0147</span>
      </li>
      <li>
        <svg viewBox="0 0 24 24"><path d="M20 4H4a2 2 0 0 0-2 2v12a2 2 0 0 0 2 2h16a2 2 0 0 0 2-2V6a2 2 0 0 0-2-2zm0 4-8 5-8-5V6l8 5 8-5z"/></svg>
        <span>rdunmore@tramvexa-mail.com</span>
      </li>
    </ul>
    <span class="stripe stripe-red"></span>
    <span class="stripe stripe-navy"></span>
  </section>

  <section class="card card-back" aria-label="Business card back">
    <div class="brand">
      <span class="brand-mark"></span>
      <span class="brand-name">Tramvexa</span>
    </div>
  </section>
</main>
</body>
</html>
```